Roofing Contractor business card redesign

I want to redesign my business card with a fresh, eye catching concept

Target Market(s)

Residential Roofing Clients, potential employees, and subcontractors.

Industry/Entity Type

Business

Colors

Designer to choose colors to be used in the design.

Requirements
Nice to have
• I just want something that's more pleasing to the eye. You can use a combination of either / or of my logos.

```html
<!DOCTYPE html>
<html lang="en">
<head>
<meta charset="utf-8">
<title>Steadfast Builders – Business Card</title>
<link rel="stylesheet" href="https://fonts.googleapis.com/css2?family=Roboto:wght@400;500&family=Roboto+Condensed:wght@700&family=Open+Sans:wght@700&display=swap">
<style>
  :root {
    --page-bg: #e8e3dd;
    --card-dark: #1a1c1e;
    --card-light: #f4f3f2;
    --brown: #4a1a12;
    --orange: #e8731f;
    --text-grey: #555555;
    --white: #ffffff;
    --emblem-a: #f2c230;
    --emblem-b: #5b2a1e;
    --art-a: rgba(232, 115, 31, 0.12);
    --art-b: rgba(90, 50, 30, 0.08);
  }
  * { margin: 0; padding: 0; box-sizing: border-box; }
  html, body { width: 1200px; height: 960px; overflow: hidden; }
  body { background: var(--page-bg); position: relative; font-family: "Roboto", Arial, sans-serif; }

  .card { position: absolute; left: 320px; width: 600px; border-radius: 20px; overflow: hidden; box-shadow: 0 6px 14px rgba(0,0,0,0.25); }
  .card-front { top: 108px; height: 340px; background: var(--card-dark); }
  .card-back { top: 493px; height: 342px; background: var(--card-light); }

  .emblem { position: absolute; left: 215px; top: 58px; width: 190px; height: 190px; border-radius: 50%;
            border: 5px solid var(--white);
            background: radial-gradient(circle at 50% 40%, var(--orange) 0%, var(--emblem-b) 70%, var(--emblem-a) 100%); }
  .front-url { position: absolute; left: 0; right: 0; top: 279px; text-align: center; color: var(--white);
               font-size: 14px; letter-spacing: 5px; }

  .back-art { position: absolute; right: 0; top: 40px; width: 290px; height: 302px;
              background: linear-gradient(160deg, var(--art-b), var(--art-a)); border-top-left-radius: 120px; }

  .brand { position: absolute; left: 30px; top: 30px; display: flex; align-items: center; gap: 10px; }
  .brand-mark { width: 36px; height: 36px; border-radius: 50%; background: var(--orange); }
  .brand-name { font-family: "Roboto Condensed", Arial, sans-serif; font-weight: 700; font-size: 40px; color: var(--brown); letter-spacing: -0.5px; }
  .brand-sub { position: absolute; left: 31px; top: 84px; font-family: "Open Sans", Arial, sans-serif; font-weight: 700; font-size: 18px; color: var(--brown); }

  .person { position: absolute; left: 29px; top: 127px; }
  .person-name { font-family: "Roboto Condensed", Arial, sans-serif; font-weight: 700; font-size: 21px; color: var(--brown); }
  .person-role { font-size: 15px; color: var(--orange); line-height: 19px; }
  .address { margin-top: 7px; font-size: 14.5px; color: var(--text-grey); line-height: 19px; }
  .contacts { list-style: none; margin-top: 9px; font-size: 14.5px; color: var(--text-grey); }
  .contacts li { display: flex; align-items: center; height: 19px; gap: 8px; }
  .contacts svg { width: 13px; height: 13px; fill: var(--brown); flex: none; }
</style>
</head>
<body>
  <section class="card card-front">
    <div class="emblem" role="img" aria-label="Circular company emblem illustration of three contractors with tools"></div>
    <p class="front-url">www.steadfastbuildtx.com</p>
  </section>

  <section class="card card-back">
    <div class="back-art" role="img" aria-label="Faint illustration of three contractors with tools"></div>
    <div class="brand">
      <span class="brand-name">Steadfast</span>
      <span class="brand-mark"></span>
      <span class="brand-name">Builders</span>
    </div>
    <p class="brand-sub">General Contractors, Inc.</p>

    <div class="person">
      <p class="person-name">SAM WHITLOCK</p>
      <p class="person-role">Keystone Certified Roof Inspector</p>
      <p class="person-role">Licensed Property Adjuster</p>
      <p class="address">4810 Meadow Lane Suite 112<br>Dallas, TX 75230</p>
      <ul class="contacts">
        <li><svg viewBox="0 0 16 16"><path d="M3 1l3 3-1.5 2c1 2 3 4 5 5L11.5 9.5l3 3L13 15C7 15 1 9 1 3z"/></svg>(555) 014-2000</li>
        <li><svg viewBox="0 0 16 16"><path d="M4 0h8a1 1 0 0 1 1 1v14a1 1 0 0 1-1 1H4a1 1 0 0 1-1-1V1a1 1 0 0 1 1-1zm1 2v10h6V2zm3 11a1 1 0 1 0 0 2 1 1 0 0 0 0-2z"/></svg>(555) 014-7731</li>
        <li><svg viewBox="0 0 16 16"><path d="M1 3h14v10H1zm1 1.5V5l6 4 6-4v-.5z"/></svg>sam@steadfastbuildtx.com</li>
        <li><svg viewBox="0 0 16 16"><circle cx="8" cy="8" r="7"/><path d="M1 8h14M8 1c-3 3-3 11 0 14M8 1c3 3 3 11 0 14" stroke="#f4f3f2" stroke-width="1.2" fill="none"/></svg>www.steadfastbuildtx.com</li>
      </ul>
    </div>
  </section>
</body>
</html>
```